Packaging design pot 500gr Polynesian honey

Task Description

Concept of design:

"This Polynesian island is a small piece of paradise nestled in the South Pacific, away from any form of civilization ( ideal place for producing honey of excellence )
= Images / symbols that induces dreaming)); (100% organic, 100% natural organic Honey logo)
Elegant, subtle , eyes catching, NO pictures of bees , Simple colors: BLACK, GOLD, WHITE, tranparency . (Designer discretion)
(Bio label optional )

the Labels: Hex1 product of TAHITI header: VELINOA HONEY (brand name) MAY USE all images herein below , free of copyright (Macro coconut flower, coconut white sand beach, exoticism; 500 gr; text on back (see attached text); Position the bar code vertically on the back; Mandatory address: Website on the back, infocontact, registration number.

500g pot :
HEIGHT With cap 12.00cm Without cap 11.85 cm
outside diameter 7.24cm
Label height should only be = 5, 1 cm x height
See the container with black cap.

Deadline
March 15, 2018 ( postpone if needed )
Updates

To all participants, i have added a personal photo you may want to consider in your creative process. If the upper section of the photo is exploited, I thought it has something interesting to bring: blue sky on the background including a shadow ot the coconut leaves, ( no bees please).

Finally i have added the colour of Velinoa Honey

Dear participants, I have updated two files to be taken into account onward : 1) final text: in French ; the replicate is English for the English version valid with the identical Graphic design 2) the true colours of Velinoa Honey, for your consideration. I thought that with the help of day light i could enhance its true body colour. Best regards, Mr KOR

Target Market(s)

Target the Asian market , Onward The US MARKET, (LUXURY oriented)

Font styles to use
Serif

Colors

Designer to choose colors to be used in the design.

Requirements
Must have
• Website address on the back, infocontact, registration number,
• texte ( summary )
• coconut tree honey ( ORIGIN )
• Color code : BLACK , GOLD , light , transparency
• COLORS THAT MATCH COLOR OF THE HONEY : DARK RED AMBER SEE IMAGE ATTACHED
Nice to have
• A matching logo
• A 400g Squezze bottle format ;
• h18.5*d7.8*c3.2(cm)
Should not have
• No Bees

```html
<!DOCTYPE html>
<html lang="fr">
<head>
<meta charset="utf-8">
<title>Cocotier Tahiti – Miel de fleur, label 500ML</title>
<link rel="stylesheet" href="https://fonts.googleapis.com/css2?family=Cinzel:wght@400;500&family=Great+Vibes&family=Roboto+Condensed:wght@300;400&display=swap">
<style>
  :root {
    --paper: #ffffff;
    --label-black: #1b1b1b;
    --label-black-deep: #121212;
    --gold: #e2b318;
    --silver-light: #f4f4f4;
    --silver-mid: #b9b9b9;
    --silver-dark: #8a8a8a;
    --text-soft: #d9d9d9;
    --flower-light: #e4d98a;
    --flower-mid: #b9a640;
    --flower-dark: #6f6a22;
  }
  * { margin: 0; padding: 0; box-sizing: border-box; }
  html, body {
    width: 903px; height: 1200px; overflow: hidden;
    background: var(--paper);
  }
  .canvas {
    position: relative;
    width: 903px; height: 1200px;
    background: var(--paper);
  }

  /* label bands */
  .label-band {
    position: absolute; left: 232px; top: 350px;
    width: 470px; height: 338px;
    background:
      repeating-linear-gradient(135deg, rgba(255,255,255,0.025) 0 2px, transparent 2px 6px),
      linear-gradient(180deg, var(--label-black), var(--label-black-deep));
  }
  .label-divider {
    position: absolute; left: 232px; top: 688px;
    width: 470px; height: 3px;
    background: var(--gold);
  }
  .label-photo {
    position: absolute; left: 232px; top: 691px;
    width: 470px; height: 179px;
    background: radial-gradient(ellipse at 50% 40%, var(--flower-light) 0%, var(--flower-mid) 45%, var(--flower-dark) 100%);
  }

  /* vertical ribbon */
  .ribbon {
    position: absolute;
    left: 431px; top: 116px;
    width: 72px; height: 272px;
    background: var(--label-black);
    border-left: 3px solid var(--gold);
    border-right: 3px solid var(--gold);
    display: flex; justify-content: center; align-items: flex-start;
    padding-top: 92px;
    gap: 3px;
    z-index: 2;
  }
  .ribbon-origin, .ribbon-made {
    writing-mode: vertical-rl;
    transform: rotate(180deg);
    white-space: nowrap;
    line-height: 1;
  }
  .ribbon-origin {
    font-family: "Cinzel", serif;
    font-size: 34px; letter-spacing: 1px;
    color: var(--silver-light);
  }
  .ribbon-made {
    font-family: "Roboto Condensed", sans-serif;
    font-size: 9px; letter-spacing: 3px;
    color: var(--gold);
    padding-top: 4px;
  }

  /* brand seal: plain circle holding the name */
  .brand {
    position: absolute;
    left: 411px; top: 372px;
    width: 112px; height: 112px; border-radius: 50%;
    background: var(--label-black);
    border: 3px solid var(--gold);
    display: flex; align-items: center; justify-content: center;
    text-align: center;
    z-index: 3;
  }
  .brand-name {
    font-family: "Cinzel", serif;
    font-size: 12px; letter-spacing: 2px; line-height: 1.5;
    color: var(--gold);
  }

  /* product text */
  .product-name {
    position: absolute; left: 0; top: 494px; width: 934px;
    text-align: center;
    font-family: "Cinzel", serif;
    font-weight: 400;
    font-size: 62px; letter-spacing: 2px; line-height: 1;
    background: linear-gradient(180deg, var(--silver-light) 0%, var(--silver-mid) 55%, var(--silver-dark) 100%);
    -webkit-background-clip: text; background-clip: text;
    color: transparent;
  }
  .product-origin {
    position: absolute; left: 0; top: 566px; width: 934px;
    display: flex; justify-content: center; align-items: center; gap: 14px;
  }
  .product-origin-text {
    font-family: "Great Vibes", cursive;
    font-size: 36px; line-height: 1;
    color: var(--gold);
  }
  .dot {
    width: 10px; height: 10px; border-radius: 50%;
    border: 2px solid var(--gold);
  }
  .product-type {
    position: absolute; left: 0; top: 612px; width: 934px;
    text-align: center;
    font-family: "Roboto Condensed", sans-serif;
    font-weight: 300;
    font-size: 16px; line-height: 1; color: var(--text-soft);
  }
  .product-volume {
    position: absolute; left: 418px; top: 643px;
    width: 98px; height: 28px;
    text-align: center;
  }
  .product-volume svg { position: absolute; inset: 0; }
  .product-volume span {
    position: relative;
    display: block; line-height: 28px;
    font-family: "Roboto Condensed", sans-serif;
    font-size: 15px; color: var(--silver-light);
  }
</style>
</head>
<body>
<main class="canvas">
  <div class="label-band"></div>
  <div class="label-divider"></div>
  <div class="label-photo" role="img" aria-label="Macro photograph of coconut palm flowers, pale yellow blossoms on green stems"></div>

  <div class="ribbon">
    <span class="ribbon-origin">TAHITI</span>
    <span class="ribbon-made">MADE IN FRENCH</span>
  </div>

  <div class="brand">
    <span class="brand-name">VELINOA<br>HONEY</span>
  </div>

  <h1 class="product-name">COCOTIER</h1>
  <div class="product-origin">
    <span class="dot"></span>
    <span class="product-origin-text">Tahiti</span>
    <span class="dot"></span>
  </div>
  <p class="product-type">Miel de fleur</p>
  <div class="product-volume">
    <svg viewBox="0 0 98 28" width="98" height="28" aria-hidden="true">
      <polygon points="2,2 96,2 89,14 96,26 2,26 9,14" fill="none" stroke="#e2b318" stroke-width="1.5"/>
    </svg>
    <span>500ML</span>
  </div>
</main>
</body>
</html>
```